Business card for a Exhibition booth fabrication company

Hi. My company would like to change our corporate name card. We are an events and Exhibition stand builder company. We would like our corporate name card to resonate what we do. I need someone to create something unique that relates to the industry that I am in. The graphic designer should be creative to incorporate the elements of my industry and try to blend in well in the design of the card. Our aim is to ensure that we are unique and our card can look different from our competitors.
Updates

The decision maker was very busy and didnt had time to make this decision

Target Market(s)

Marketing and events manager from all companies

Contact Information for Business Card

The business card should have the following details:
Name
Job Title
Email
Website

Colors

Designer to choose colors to be used in the design.

Requirements
Must have
• The card must be look something that is relevant to the service that I am providing. My website is: www.velmora-buildworks.example
• You can see my website to get more information on what service that I am doing
Nice to have
• On the back of my card, I would like to have a globe image with the incorporation of my company logo. This is to indicate that my services can be done in any part of the world.

```html
<!DOCTYPE html>
<html lang="en">
<head>
<meta charset="utf-8">
<title>Velmora Buildworks – Business Card</title>
<link rel="stylesheet" href="https://fonts.googleapis.com/css2?family=Montserrat:wght@400;500;700&display=swap">
<style>
  :root {
    --page: #1b1b1d;
    --card: #232426;
    --card-edge: #2c2d30;
    --accent: #e0242b;
    --text: #f2f2f2;
    --muted: #b9b9bb;
    --map: #2b2c2f;
  }
  * { box-sizing: border-box; margin: 0; padding: 0; }
  html, body { width: 1200px; height: 800px; overflow: hidden; }
  body {
    background: var(--page);
    font-family: "Montserrat", sans-serif;
    color: var(--text);
    display: flex;
    align-items: center;
    justify-content: center;
    gap: 36px;
  }
  .card {
    width: 548px;
    height: 312px;
    background: var(--card);
    border: 1px solid var(--card-edge);
    border-radius: 22px;
    position: relative;
    overflow: hidden;
    box-shadow: 0 18px 40px rgba(0,0,0,.5);
  }

  /* Services side */
  .world-map {
    position: absolute;
    inset: 40px 50px;
    border-radius: 40px;
    background: radial-gradient(ellipse at center, var(--map) 0%, rgba(43,44,47,0) 75%);
  }
  .services {
    position: absolute;
    inset: 0;
    padding: 0 28px;
    display: flex;
    flex-direction: column;
    align-items: center;
    justify-content: center;
    text-align: center;
    gap: 6px;
  }
  .services-title {
    color: var(--accent);
    font-weight: 700;
    font-size: 22px;
    letter-spacing: 1px;
    margin-bottom: 8px;
  }
  .services-line {
    font-size: 13px;
    font-weight: 500;
    line-height: 1.45;
    color: var(--text);
  }

  /* Contact side */
  .brand {
    position: absolute;
    left: 32px;
    bottom: 56px;
    display: flex;
    align-items: center;
    gap: 10px;
  }
  .brand-dot {
    width: 28px; height: 28px;
    border-radius: 50%;
    background: var(--accent);
    flex: none;
  }
  .brand-name {
    font-weight: 700;
    font-size: 14px;
    letter-spacing: 1.2px;
    color: var(--text);
    white-space: nowrap;
  }
  .divider {
    position: absolute;
    left: 282px;
    top: 48px;
    width: 1.5px;
    height: 160px;
    background: linear-gradient(var(--accent), rgba(224,36,43,.2));
  }
  .contact {
    position: absolute;
    left: 298px;
    top: 56px;
    right: 24px;
  }
  .contact-name {
    color: var(--accent);
    font-weight: 700;
    font-size: 21px;
  }
  .contact-role {
    font-size: 12px;
    color: var(--muted);
    margin-bottom: 22px;
  }
  .contact-list { list-style: none; display: flex; flex-direction: column; gap: 9px; }
  .contact-item {
    display: flex;
    align-items: center;
    gap: 7px;
    font-size: 10.5px;
    font-weight: 500;
    white-space: nowrap;
  }
  .contact-item svg { width: 11px; height: 11px; flex: none; fill: var(--accent); }
</style>
</head>
<body>
  <section class="card card--services">
    <div class="world-map" role="img" aria-label="Faint world map in the card background"></div>
    <div class="services">
      <h2 class="services-title">OUR SERVICES</h2>
      <p class="services-line">Exhibition Booth Fabrication | Outdoor Booth Setup | Interior Design</p>
      <p class="services-line">Installation and Dismantle | Exhibition Management</p>
      <p class="services-line">Shell Scheme Display Booth | Custom Stand Design</p>
      <p class="services-line">Exhibition Furniture and Equipment | Exhibition Project Management</p>
    </div>
  </section>

  <section class="card card--contact">
    <div class="brand">
      <span class="brand-dot"></span>
      <span class="brand-name">VELMORA BUILDWORKS</span>
    </div>
    <div class="divider"></div>
    <div class="contact">
      <h1 class="contact-name">Aren Dalby</h1>
      <p class="contact-role">Director</p>
      <ul class="contact-list">
        <li class="contact-item">
          <svg viewBox="0 0 24 24" aria-hidden="true"><path d="M6.6 10.8a15.2 15.2 0 0 0 6.6 6.6l2.2-2.2a1 1 0 0 1 1-.25 11.4 11.4 0 0 0 3.6.57 1 1 0 0 1 1 1V20a1 1 0 0 1-1 1A17 17 0 0 1 3 4a1 1 0 0 1 1-1h3.5a1 1 0 0 1 1 1c0 1.25.2 2.450.57 3.57a1 1 0 0 1-.25 1z"/></svg>
          0100 555 274
        </li>
        <li class="contact-item">
          <svg viewBox="0 0 24 24" aria-hidden="true"><path d="M2 5h20v14H2zm2 2v.5l8 5 8-5V7l-8 5z"/></svg>
          info@velmora-buildworks.example
        </li>
        <li class="contact-item">
          <svg viewBox="0 0 24 24" aria-hidden="true"><circle cx="12" cy="12" r="10"/></svg>
          www.velmora-buildworks.example
        </li>
      </ul>
    </div>
  </section>
</body>
</html>
```